Heron Yards LLC - Door Hanger for Residential Mowing

Door Hanger- Heron Yards LLC. I would like the Heron Logo on a white background with three shades of pink incorporated into the flyer. Our phone number is 352-408-7716. And our website is heronyardcare.net. I would like for the door hanger to mirror the Copperfield Door Hanger, using the Heron logo & information.

List of Services to include:
Pest Control
Termite Inspection
Lawn Maintenance
Debris Clean-up
Trash Removal
Home Inspection
Handy-man Services

Target Market(s)

Residential Lawns

Industry/Entity Type

Lawn Care

Font styles to use
Sans Serif

Colors
e34197
e667a6
eea4c8
f9d9e8

Requirements
Must have
• Phone Number
• Must be a Door Hanger
• Website
• 2 Sided
Nice to have
• 3 Shades of Pink with white background
Should not have
• It must be a door hanger. KEEP IN MIND THERE WILL BE A PUNCH HOLE AT TOP.......

```html
<!DOCTYPE html>
<html lang="en">
<head>
<meta charset="utf-8">
<title>Heron Yards – Door Hanger</title>
<link rel="stylesheet" href="https://fonts.googleapis.com/css2?family=Montserrat:wght@400;500&family=Oswald:wght@500&display=swap">
<style>
  :root {
    --pink-deep: #e34197;
    --pink-mid: #e667a6;
    --pink-soft: #eea4c8;
    --pink-blush: #f9d9e8;
    --white: #ffffff;
    --ink: #111111;
    --grass: #3db54a;
    --canvas: #ffffff;
  }
  * { margin: 0; padding: 0; box-sizing: border-box; }
  html, body { width: 1200px; height: 1000px; overflow: hidden; background: var(--canvas); }
  .canvas { position: relative; width: 1200px; height: 1000px; }

  .hanger {
    position: absolute; top: 30px; width: 404px; height: 940px; overflow: hidden;
    background: linear-gradient(to bottom,
      #ec7fb3 0%, var(--pink-soft) 14%, var(--pink-blush) 26%, var(--white) 33%,
      var(--pink-blush) 42%, var(--pink-soft) 52%, var(--pink-mid) 62%, #e4579f 75%, #e4579f 100%);
    font-family: "Montserrat", sans-serif;
    text-align: center;
  }
  .hanger--front { left: 136px; }
  .hanger--back { left: 660px; }

  .punch-hole {
    position: absolute; left: 132px; top: 53px; width: 140px; height: 140px;
    border-radius: 50%; background: var(--white);
  }

  .brand {
    position: absolute; left: 0; right: 0; top: 276px; height: 50px;
    display: flex; align-items: center; justify-content: center; gap: 14px;
  }
  .brand-dot { width: 44px; height: 44px; border-radius: 50%; background: var(--pink-deep); flex: none; }
  .brand-name {
    font-family: "Montserrat", sans-serif; font-weight: 500; font-size: 30px;
    letter-spacing: 2px; color: var(--ink); line-height: 1; white-space: nowrap;
  }

  .headline { position: absolute; left: 0; right: 0; color: var(--ink); font-weight: 500; line-height: 1.2; }
  .hanger--front .headline { top: 470px; font-size: 33px; letter-spacing: 1px; }
  .hanger--back .headline { top: 501px; font-size: 31px; }

  .blurb {
    position: absolute; left: 20px; right: 20px; top: 529px;
    font-size: 17px; line-height: 25px; color: #2a1a22;
  }
  .blurb span { display: block; white-space: nowrap; }

  .price-box {
    position: absolute; left: 42px; top: 635px; width: 330px; height: 102px;
    background: var(--white); border-radius: 12px;
  }
  .price-symbol { position: absolute; left: 14px; top: 28px; font-size: 42px; color: var(--pink-deep); line-height: 1.1; }
  .price-unit { position: absolute; right: 16px; bottom: 8px; font-size: 13px; color: var(--pink-deep); }

  .service-list {
    position: absolute; left: 98px; top: 558px; list-style: none; text-align: left;
    font-size: 20px; line-height: 25px; color: var(--ink);
  }
  .service-list li::before { content: "• "; }

  .cta { position: absolute; left: 0; right: 0; top: 763px; font-size: 22px; line-height: 1.2; color: var(--white); }
  .phone {
    position: absolute; left: 0; right: 0; top: 784px;
    font-family: "Oswald", sans-serif; font-weight: 500; font-size: 60px; line-height: 1;
    color: var(--white); letter-spacing: 0.5px;
  }

  .grass { position: absolute; left: 0; bottom: 0; width: 404px; height: 92px; }
  .website {
    position: absolute; left: 0; right: 0; top: 893px;
    font-size: 16px; font-weight: 500; line-height: 1; color: var(--white); letter-spacing: 0.5px;
  }
</style>
</head>
<body>
<div class="canvas">

  <section class="hanger hanger--front">
    <div class="punch-hole"></div>
    <div class="brand">
      <span class="brand-dot"></span>
      <span class="brand-name">HERON YARDS</span>
    </div>
    <h2 class="headline">LAWN MOWING</h2>
    <p class="blurb">
      <span>We keep your lawn green,</span>
      <span>healthy and free of weeds.</span>
      <span>Aeration, Fertilization and reg-</span>
      <span>ular landscaping services.</span>
    </p>
    <div class="price-box">
      <span class="price-symbol">$</span>
      <span class="price-unit">per service</span>
    </div>
    <p class="cta">call to schedule service today</p>
    <p class="phone">352-408-7716</p>
    <svg class="grass" viewBox="0 0 404 92" role="img" aria-label="Green grass blades along the bottom edge">
      <rect x="0" y="26" width="404" height="66" fill="var(--grass)"/>
    </svg>
    <p class="website">heronyardcare.net</p>
  </section>

  <section class="hanger hanger--back">
    <div class="punch-hole"></div>
    <div class="brand">
      <span class="brand-dot"></span>
      <span class="brand-name">HERON YARDS</span>
    </div>
    <h2 class="headline">Additional services:</h2>
    <ul class="service-list">
      <li>Pest Control</li>
      <li>Termite Inspection</li>
      <li>Lawn Maintenance</li>
      <li>Debris Clean-up</li>
      <li>Trash Removal</li>
      <li>Home Inspection</li>
      <li>Handy-man Services</li>
    </ul>
    <p class="cta">call today for a free estimate</p>
    <p class="phone">352-408-7716</p>
    <svg class="grass" viewBox="0 0 404 92" role="img" aria-label="Green grass blades along the bottom edge">
      <rect x="0" y="26" width="404" height="66" fill="var(--grass)"/>
    </svg>
    <p class="website">heronyardcare.net</p>
  </section>

</div>
</body>
</html>
```